Real Estate Investment Company

Design Powerpoint slides are consistent with our logo, colors, and typeface. These Powerpoint slides will be used in all aspects of the business from live presentations to presentation decks available on a website or via email. Need to have different slide types created that allow for different types of slides such as cover pages, text heavy pages, image and chart heavy pages, multiple column pages, and mixed content pages.

Reason: to give additional time to get the design correct. I plan on making a selection in the next day or 2

Target Market(s)

Real Estate Investors

Industry/Entity Type

Investment

Other font styles liked:
• Consistent with logo

Requirements
Must have
• Our colors
• Our logo where possible
• Different slide designs of the same theme to allow for different types of slides such as cover pages, text heavy, picture heavy, and mixed content.
• Slides in both portrait and landscape orientation
Nice to have

```html
<!DOCTYPE html>
<html lang="en">
<head>
<meta charset="utf-8">
<title>Keystone Holdings — Presentation Slide System</title>
<link href="https://fonts.googleapis.com/css2?family=Oswald:wght@500;600&family=Open+Sans:wght@400;600;700&display=swap" rel="stylesheet">
<style>
  :root{
    --navy:#25337a;
    --navy-dark:#1c275f;
    --blue:#3552a3;
    --blue-mid:#5a6fb6;
    --blue-soft:#8c9bd0;
    --blue-pale:#d9deef;
    --ink:#2a2a2a;
    --grey:#666a75;
    --canvas:#e6e8ee;
    --white:#ffffff;
    --green:#3aa64a;
    --teal:#3fb6c8;
  }
  *{box-sizing:border-box;margin:0;padding:0}
  html,body{width:1200px;height:2715px;overflow:hidden;background:var(--canvas)}
  body{font-family:"Open Sans",Arial,sans-serif;color:var(--ink)}
  .deck{display:grid;grid-template-columns:585px 585px;grid-auto-rows:328px;gap:10px;padding:10px;width:1200px;height:2715px}
  .slide{position:relative;background:var(--white);overflow:hidden}
  .slide-title{position:absolute;top:18px;left:0;right:0;text-align:center;font-family:"Oswald",sans-serif;font-weight:600;font-size:16px;color:var(--navy);letter-spacing:.3px;text-transform:uppercase}
  .title-rule{position:absolute;top:44px;left:50%;width:70px;margin-left:-35px;height:2px;background:var(--navy)}
  .title-rule::after{content:"";position:absolute;left:50%;top:-4px;margin-left:-5px;width:10px;height:10px;border-radius:50%;background:var(--navy)}
  .foot-rule{position:absolute;left:0;right:0;bottom:20px;height:2px;background:var(--navy)}
  .foot-rule::after{content:"";position:absolute;right:88px;top:-4px;width:10px;height:10px;border-radius:50%;background:var(--white);border:2px solid var(--navy)}
  .brand{position:absolute;right:12px;bottom:26px;display:flex;align-items:center;gap:4px;font-family:"Oswald",sans-serif;font-weight:600;font-size:8.5px;color:var(--navy);letter-spacing:.3px}
  .brand-mark{width:14px;height:14px;background:var(--navy)}
  .body-text{font-size:7px;line-height:1.45;color:var(--grey)}
  .lead{font-size:10px;font-weight:700;color:var(--navy);line-height:1.25}
  .photo{position:absolute}
  .white{color:var(--white)}

  .cover{background:linear-gradient(135deg,#2c3c8a 0%,#1f2b68 60%,#283777 100%)}
  .cover-band{position:absolute;left:0;right:0;top:112px;height:88px;background:var(--blue);opacity:.92;display:flex;flex-direction:column;justify-content:center;align-items:center}
  .cover-title{font-weight:700;font-size:21px;color:var(--white)}
  .cover-sub{font-weight:700;font-size:17px;color:var(--white)}

  .toc{position:absolute;top:70px;left:80px;right:30px;display:grid;grid-template-columns:1fr 1fr;row-gap:14px;column-gap:30px}
  .toc-item{display:flex;gap:12px;align-items:flex-start}
  .toc-dot{flex:none;width:26px;height:26px;border-radius:50%;background:var(--white);border:2px solid var(--navy);display:flex;align-items:center;justify-content:center}
  .toc-dot::after{content:"";width:12px;height:12px;border-radius:50%;background:var(--navy)}
  .toc-head{font-size:9px;font-weight:700;color:var(--navy)}

  .data-table{position:absolute;top:86px;left:95px;width:395px;border-collapse:collapse;font-size:6.5px;color:var(--white)}
  .data-table th{background:var(--navy-dark);font-weight:700;padding:4px;border:1px solid var(--white)}
  .data-table td{background:var(--blue);padding:7px 10px;border:1px solid var(--white);line-height:1.4;font-weight:600}

  .team{position:absolute;top:80px;left:145px;display:flex;gap:28px}
  .member{width:80px;font-size:7px;color:var(--grey);line-height:1.35}
  .avatar{width:72px;height:72px;border-radius:50%;background:var(--navy);border:4px solid var(--blue-pale);margin-bottom:8px}
  .member b{display:block;color:var(--ink);font-size:8px}
  .stars{color:var(--green);font-size:9px;letter-spacing:1px}

  .section{background:var(--navy)}
  .section-label{position:absolute;left:0;width:270px;top:200px;text-align:center;color:var(--white);font-size:30px}

  .thanks{background:var(--blue)}
  .thanks-word{position:absolute;top:0;left:0;right:0;height:160px;display:flex;align-items:center;justify-content:center;color:var(--white);font-weight:700;font-size:27px}
  .thanks-band{position:absolute;left:0;right:0;bottom:0;height:140px;background:var(--navy)}
  .social{position:absolute;left:50%;top:58px;transform:translateX(-50%);display:flex;gap:8px}
  .social span{width:24px;height:24px;border-radius:3px;background:var(--blue-soft)}
</style>
</head>
<body>
<main class="deck">

  <section class="slide cover">
    <div class="photo" role="img" aria-label="Faint photograph of city towers behind the cover" style="inset:0;background:linear-gradient(120deg,rgba(255,255,255,.06),rgba(255,255,255,0) 50%,rgba(255,255,255,.05))"></div>
    <div class="cover-band">
      <div class="cover-title">PRESENTATION TITLE HERE</div>
      <div class="cover-sub">Sub Title Here</div>
    </div>
  </section>

  <section class="slide">
    <h2 class="slide-title">Table of Contents</h2><div class="title-rule"></div>
    <div class="toc">
      <div class="toc-item"><div class="toc-dot"></div><div><div class="toc-head">Content Here</div><p class="body-text">Short summary of this part of the deck, written in two brief lines.</p></div></div>
      <div class="toc-item"><div class="toc-dot"></div><div><div class="toc-head">Content Here</div><p class="body-text">Short summary of this part of the deck, written in two brief lines.</p></div></div>
      <div class="toc-item"><div class="toc-dot"></div><div><div class="toc-head">Content Here</div><p class="body-text">Short summary of this part of the deck, written in two brief lines.</p></div></div>
      <div class="toc-item"><div class="toc-dot"></div><div><div class="toc-head">Content Here</div><p class="body-text">Short summary of this part of the deck, written in two brief lines.</p></div></div>
      <div class="toc-item"><div class="toc-dot"></div><div><div class="toc-head">Content Here</div><p class="body-text">Short summary of this part of the deck, written in two brief lines.</p></div></div>
      <div class="toc-item"><div class="toc-dot"></div><div><div class="toc-head">Content Here</div><p class="body-text">Short summary of this part of the deck, written in two brief lines.</p></div></div>
    </div>
    <div class="foot-rule"></div>
    <div class="brand"><span class="brand-mark"></span>KEYSTONE HOLDINGS</div>
  </section>

  <section class="slide">
    <h2 class="slide-title">About Us</h2><div class="title-rule"></div>
    <div style="position:absolute;top:64px;left:30px;width:235px">
      <p class="lead">Lorem ipsum dolor sit amet, consectetur adipiscing elit.</p>
      <p class="body-text" style="margin-top:8px">We acquire, improve and hold income property across growing markets. Our team studies each site, secures fair terms and manages every asset with care, so investors see steady returns and clear reports through each stage of the holding period.</p>
      <p class="body-text" style="margin-top:8px">Every deal is measured against long term value, local demand and risk. We share data openly, keep costs lean and work with trusted partners on build, lease and sale, giving each investor a simple view of how their capital performs.</p>
    </div>
    <div class="photo" role="img" aria-label="Photograph of a modern city skyline beside a river" style="top:72px;left:280px;width:270px;height:170px;background:linear-gradient(180deg,#9fc0e0 0%,#c9d6e2 50%,#6f8a6a 80%,#4c6e8c 100%)"></div>
    <div class="foot-rule"></div>
    <div class="brand"><span class="brand-mark"></span>KEYSTONE HOLDINGS</div>
  </section>

  <section class="slide">
    <h2 class="slide-title">Our Vision</h2><div class="title-rule"></div>
    <div style="position:absolute;top:120px;left:300px;right:0;height:70px;background:var(--blue-mid)"></div>
    <svg style="position:absolute;left:0;top:0" width="585" height="328" viewBox="0 0 585 328">
      <circle cx="240" cy="155" r="108" fill="#fff" stroke="#eceff6" stroke-width="10"/>
      <circle cx="195" cy="155" r="48" fill="#25337a"/>
      <circle cx="280" cy="155" r="48" fill="#3552a3"/>
    </svg>
    <div class="white" style="position:absolute;left:160px;top:130px;width:70px;font-size:6.5px;line-height:1.35"><b style="font-size:8px">Vision</b><br>Lead the region in value driven property growth.</div>
    <div class="white" style="position:absolute;left:248px;top:130px;width:70px;font-size:6.5px;line-height:1.35"><b style="font-size:8px">Mision</b><br>Build lasting wealth for every partner we serve.</div>
    <div class="foot-rule"></div>
    <div class="brand"><span class="brand-mark"></span>KEYSTONE HOLDINGS</div>
  </section>

  <section class="slide">
    <h2 class="slide-title">Our Process</h2><div class="title-rule"></div>
    <svg style="position:absolute;left:0;top:0" width="585" height="328" viewBox="0 0 585 328">
      <g fill="#25337a">
        <polygon points="163,147 194,165 194,199 163,217 132,199 132,165"/>
        <polygon points="230,112 261,130 261,164 230,182 199,164 199,130"/>
        <polygon points="302,147 333,165 333,199 302,217 271,199 271,165"/>
        <polygon points="371,112 402,130 402,164 371,182 340,164 340,130"/>
        <polygon points="440,147 471,165 471,199 440,217 409,199 409,165"/>
      </g>
      <g fill="#fff">
        <circle cx="156" cy="177" r="3"/><circle cx="170" cy="177" r="3"/><circle cx="163" cy="175" r="3.5"/>
        <rect x="152" y="182" width="22" height="7" rx="2"/>
        <rect x="219" y="136" width="9" height="9" rx="2" fill="none" stroke="#fff" stroke-width="2"/>
        <rect x="232" y="136" width="9" height="9" rx="2" fill="none" stroke="#fff" stroke-width="2"/>
        <rect x="219" y="149" width="9" height="9" rx="2" fill="none" stroke="#fff" stroke-width="2"/>
        <rect x="232" y="149" width="9" height="9" rx="2" fill="none" stroke="#fff" stroke-width="2"/>
        <polygon points="295,170 295,194 314,182"/>
        <rect x="360" y="140" width="22" height="16" fill="none" stroke="#fff" stroke-width="1.5"/>
        <rect x="364" y="148" width="3" height="6"/><rect x="369" y="145" width="3" height="9"/><rect x="374" y="143" width="3" height="11"/>
        <polygon points="440,168 444,178 455,178 446,185 449,196 440,189 431,196 434,185 425,178 436,178"/>
      </g>
    </svg>
    <p class="body-text" style="position:absolute;left:120px;top:228px;width:90px">Step one text about how we source the right deal.</p>
    <p class="body-text" style="position:absolute;left:195px;top:76px;width:90px">Step two text on study, numbers and local review.</p>
    <p class="body-text" style="position:absolute;left:262px;top:228px;width:90px">Step three text about buying and closing terms.</p>
    <p class="body-text" style="position:absolute;left:330px;top:76px;width:90px">Step four text on upgrades and leasing plans.</p>
    <p class="body-text" style="position:absolute;left:400px;top:228px;width:90px">Step five text on returns, reports and exit.</p>
    <div class="foot-rule"></div>
    <div class="brand"><span class="brand-mark"></span>KEYSTONE HOLDINGS</div>
  </section>

  <section class="slide">
    <h2 class="slide-title">Your Text in Two Coulumns</h2><div class="title-rule"></div>
    <div style="position:absolute;top:74px;left:90px;width:200px">
      <p class="body-text">Our portfolio spans homes, offices and mixed use sites in high growth areas. Each asset is chosen for strong demand, sound structure and room to add value. We track rent, costs and market trends each month and adjust plans early, so the holding keeps pace with the market and investors stay informed about every move we make.</p>
      <p class="body-text" style="margin-top:8px">We keep debt at safe levels and hold cash for repairs, giving each property a firm base through every cycle of the market.</p>
    </div>
    <div style="position:absolute;top:74px;left:310px;width:200px">
      <p class="body-text">Investors join through clear terms with fair fees and simple reports. We explain every step, from the first offer to the final sale, and keep our own capital in each deal beside theirs. This shared stake keeps our goals aligned and our focus on long term results rather than quick gains or short term trends in price.</p>
      <p class="body-text" style="margin-top:8px">Quarterly updates cover income, value and plans, with our team ready to answer questions at any time.</p>
    </div>
    <div class="foot-rule"></div>
    <div class="brand"><span class="brand-mark"></span>KEYSTONE HOLDINGS</div>
  </section>

  <section class="slide">
    <h2 class="slide-title">Our Services</h2><div class="title-rule"></div>
    <div class="photo" role="img" aria-label="Photograph of a person working at a laptop" style="left:50px;top:70px;width:95px;height:95px;background:linear-gradient(160deg,#cfd6e4,#7d8fb5)"></div>
    <div class="photo" role="img" aria-label="Photograph of colleagues in an office meeting" style="left:50px;top:175px;width:95px;height:95px;background:linear-gradient(160deg,#e2e5ec,#9aa6bf)"></div>
    <div style="position:absolute;left:155px;top:70px;width:115px;height:95px;background:var(--navy)">
      <svg style="position:absolute;left:45px;top:16px" width="26" height="22" viewBox="0 0 26 22"><rect x="1" y="1" width="24" height="20" fill="none" stroke="#fff" stroke-width="1.5"/><rect x="6" y="10" width="3" height="8" fill="#fff"/><rect x="11" y="7" width="3" height="11" fill="#fff"/><rect x="16" y="5" width="3" height="13" fill="#fff"/></svg>
      <p class="white" style="position:absolute;left:10px;right:10px;top:50px;font-size:6px;line-height:1.4">Asset review and value reports for each holding.</p>
    </div>
    <div style="position:absolute;left:155px;top:175px;width:115px;height:95px;background:var(--blue)">
      <svg style="position:absolute;left:44px;top:16px" width="28" height="20" viewBox="0 0 28 20"><circle cx="7" cy="6" r="3.5" fill="#fff"/><circle cx="21" cy="6" r="3.5" fill="#fff"/><circle cx="14" cy="5" r="4" fill="#fff"/><rect x="2" y="11" width="24" height="8" rx="3" fill="#fff"/></svg>
      <p class="white" style="position:absolute;left:10px;right:10px;top:50px;font-size:6px;line-height:1.4">Investor relations and shared deal planning.</p>
    </div>
    <p class="body-text" style="position:absolute;left:300px;top:74px;width:240px">We handle the full life of each asset, from search and study to purchase, upgrade and lease. Our team sets the budget, hires trusted trades and checks the work, then finds good tenants and keeps them. Clear monthly numbers show how each site performs and where we plan to add value next.</p>
    <p class="body-text" style="position:absolute;left:300px;top:178px;width:240px">For investors we offer simple entry, fair fees and open books. Each partner gets a direct contact, regular calls and full access to reports. We explain risk plainly and share both the wins and the lessons, so trust grows with every project we complete together.</p>
    <div class="foot-rule"></div>
    <div class="brand"><span class="brand-mark"></span>KEYSTONE HOLDINGS</div>
  </section>

  <section class="slide">
    <h2 class="slide-title">Three of Quality Segment</h2><div class="title-rule"></div>
    <div style="position:absolute;left:0;right:0;top:118px;height:50px;background:var(--blue-mid)"></div>
    <svg style="position:absolute;left:0;top:0" width="585" height="328" viewBox="0 0 585 328">
      <g fill="#5a6fb6"><circle cx="150" cy="143" r="52"/><circle cx="292" cy="143" r="52"/><circle cx="434" cy="143" r="52"/></g>
      <g fill="#25337a" stroke="#3552a3" stroke-width="5"><circle cx="150" cy="143" r="42"/><circle cx="292" cy="143" r="42"/><circle cx="434" cy="143" r="42"/></g>
    </svg>
    <p class="white" style="position:absolute;left:115px;top:132px;width:70px;text-align:center;font-size:6.5px;line-height:1.35">Homes in fast growing suburbs.</p>
    <p class="white" style="position:absolute;left:257px;top:132px;width:70px;text-align:center;font-size:6.5px;line-height:1.35">Offices near transit centers.</p>
    <p class="white" style="position:absolute;left:399px;top:132px;width:70px;text-align:center;font-size:6.5px;line-height:1.35">Mixed use retail and living.</p>
    <p class="body-text" style="position:absolute;left:110px;top:210px;width:365px;text-align:center">Each segment has its own targets, risk level and hold period. Together they give our portfolio balance, steady income and room to grow as local markets change over time.</p>
    <div class="foot-rule"></div>
    <div class="brand"><span class="brand-mark"></span>KEYSTONE HOLDINGS</div>
  </section>

  <section class="slide">
    <h2 class="slide-title">Table of Slide</h2><div class="title-rule"></div>
    <table class="data-table">
      <thead><tr><th>Section 1</th><th>Section 2</th><th>Section 3</th></tr></thead>
      <tbody>
        <tr><td>Entry cost, closing fees and first year repair budget for the site.</td><td>Rent roll, lease terms and average tenant stay across units.</td><td>Projected value, hold period and planned exit route for owners.</td></tr>
        <tr><td>Entry cost, closing fees and first year repair budget for the site.</td><td>Rent roll, lease terms and average tenant stay across units.</td><td>Projected value, hold period and planned exit route for owners.</td></tr>
      </tbody>
    </table>
    <div class="foot-rule"></div>
    <div class="brand"><span class="brand-mark"></span>KEYSTONE HOLDINGS</div>
  </section>

  <section class="slide">
    <h2 class="slide-title">Our Team</h2><div class="title-rule"></div>
    <div class="team">
      <div class="member"><div class="avatar" role="img" aria-label="Team member portrait"></div><b>Personal Name</b><b>Job Title</b>Short role note for this team member goes here.<div class="stars">★★★★★</div></div>
      <div class="member"><div class="avatar" role="img" aria-label="Team member portrait"></div><b>Personal Name</b><b>Job Title</b>Short role note for this team member goes here.<div class="stars">★★★★★</div></div>
      <div class="member"><div class="avatar" role="img" aria-label="Team member portrait"></div><b>Personal Name</b><b>Job Title</b>Short role note for this team member goes here.<div class="stars">★★★★<span style="color:#ccc">★</span></div></div>
    </div>
    <div class="foot-rule"></div>
    <div class="brand"><span class="brand-mark"></span>KEYSTONE HOLDINGS</div>
  </section>

  <section class="slide section">
    <svg style="position:absolute;left:90px;top:105px" width="90" height="80" viewBox="0 0 90 80">
      <circle cx="34" cy="30" r="24" fill="#dfe4f2"/>
      <circle cx="58" cy="44" r="20" fill="#3552a3" stroke="#25337a" stroke-width="3"/>
      <circle cx="28" cy="54" r="16" fill="#1c275f" stroke="#dfe4f2" stroke-width="3"/>
    </svg>
    <div class="section-label">Section</div>
  </section>

  <section class="slide">
    <h2 class="slide-title">Your Data in Pie Graph</h2><div class="title-rule"></div>
    <div style="position:absolute;left:0;right:0;top:155px;height:2px;background:var(--blue-mid)"></div>
    <svg style="position:absolute;left:0;top:0" width="585" height="328" viewBox="0 0 585 328">
      <g fill="#8c9bd0"><circle cx="80" cy="155" r="24"/><circle cx="150" cy="190" r="50"/><circle cx="250" cy="125" r="42"/><circle cx="335" cy="145" r="54"/><circle cx="495" cy="120" r="54"/><circle cx="440" cy="200" r="42"/></g>
      <g fill="#3552a3"><circle cx="80" cy="155" r="17"/><circle cx="150" cy="190" r="40"/><circle cx="250" cy="125" r="33"/><circle cx="335" cy="145" r="44"/><circle cx="495" cy="120" r="44"/><circle cx="440" cy="200" r="33"/></g>
      <g fill="#fff" font-family="Open Sans, sans-serif" text-anchor="middle">
        <text x="80" y="159" font-size="11" font-weight="700">10%</text>
        <text x="150" y="190" font-size="20">60%</text>
        <text x="250" y="132" font-size="20">35%</text>
        <text x="335" y="150" font-size="22">90%</text>
        <text x="495" y="124" font-size="22">75%</text>
        <text x="440" y="204" font-size="18">50%</text>
      </g>
      <g fill="#dfe4f2" font-family="Open Sans, sans-serif" font-size="5.5" text-anchor="middle">
        <text x="150" y="203">Share held in</text><text x="150" y="210">core homes</text>
        <text x="335" y="164">Units leased</text><text x="335" y="171">this quarter</text>
        <text x="495" y="138">Target met</text><text x="495" y="145">on returns</text>
        <text x="440" y="215">Debt ratio</text>
      </g>
      <g fill="#333" font-family="Open Sans, sans-serif" font-size="6" text-anchor="middle">
        <text x="80" y="112">This pie graph</text><text x="80" y="119">shows share</text>
        <text x="250" y="70">This pie graph</text><text x="250" y="77">shows share</text>
      </g>
    </svg>
    <div class="foot-rule"></div>
    <div class="brand"><span class="brand-mark"></span>KEYSTONE HOLDINGS</div>
  </section>

  <section class="slide">
    <div class="photo" role="img" aria-label="Photograph of a smiling business team standing together in an office" style="inset:0;background:linear-gradient(180deg,#e9eef5 0%,#c8d2e2 55%,#8796b4 100%)"></div>
    <div style="position:absolute;left:30px;top:140px;width:150px;height:160px;background:var(--navy);opacity:.92;padding:14px">
      <p class="white" style="font-size:10px;font-weight:700;line-height:1.25">Lorem ipsum dolor sit amet, consectetur.</p>
      <p class="white" style="font-size:6px;line-height:1.45;margin-top:8px">Our people bring years of local market skill, sound judgment and care to every deal we manage for our partners and investors.</p>
    </div>
  </section>

  <section class="slide">
    <h2 class="slide-title">Your Statistics in Bar Graph</h2><div class="title-rule"></div>
    <p class="lead" style="position:absolute;left:40px;top:64px">Lorem ipsum DOLOR sit amet</p>
    <svg style="position:absolute;left:30px;top:90px" width="330" height="150" viewBox="0 0 330 150">
      <g stroke="#333" stroke-width="1" fill="none">
        <path d="M12 10 V125 H100"/><path d="M122 10 V125 H210"/><path d="M232 10 V125 H320"/>
      </g>
      <g fill="#25337a">
        <rect x="20" y="95" width="11" height="30"/><rect x="36" y="70" width="11" height="55"/><rect x="52" y="55" width="11" height="70"/><rect x="68" y="40" width="11" height="85"/><rect x="84" y="18" width="11" height="107"/>
        <rect x="130" y="80" width="11" height="45"/><rect x="146" y="58" width="11" height="67"/><rect x="162" y="60" width="11" height="65"/><rect x="178" y="38" width="11" height="87"/><rect x="194" y="22" width="11" height="103"/>
        <rect x="240" y="88" width="11" height="37"/><rect x="256" y="65" width="11" height="60"/><rect x="272" y="45" width="11" height="80"/><rect x="288" y="45" width="11" height="80"/><rect x="304" y="15" width="11" height="110"/>
      </g>
      <g font-family="Open Sans, sans-serif" font-size="5" fill="#333" text-anchor="middle">
        <text x="25" y="133">A</text><text x="41" y="133">B</text><text x="57" y="133">C</text><text x="73" y="133">D</text><text x="89" y="133">E</text>
        <text x="135" y="133">A</text><text x="151" y="133">B</text><text x="167" y="133">C</text><text x="183" y="133">D</text><text x="199" y="133">E</text>
        <text x="245" y="133">A</text><text x="261" y="133">B</text><text x="277" y="133">C</text><text x="293" y="133">D</text><text x="309" y="133">E</text>
      </g>
    </svg>
    <p class="body-text" style="position:absolute;left:395px;top:110px;width:160px">Rental income rose in each market over five periods. The steady climb reflects higher occupancy, careful upgrades and longer leases. We expect growth to hold as new units come online and demand in core areas stays firm through the coming year.</p>
    <div class="foot-rule"></div>
    <div class="brand"><span class="brand-mark"></span>KEYSTONE HOLDINGS</div>
  </section>

  <section class="slide">
    <h2 class="slide-title">Your Statistic in Line Graph</h2><div class="title-rule"></div>
    <p class="lead" style="position:absolute;left:40px;top:64px">Lorem IPSUM dolor sit amet.</p>
    <svg style="position:absolute;left:30px;top:82px" width="240" height="180" viewBox="0 0 240 180">
      <g stroke="#333" stroke-width="1" fill="none"><path d="M14 6 V150 H232"/></g>
      <g font-family="Open Sans, sans-serif" font-size="5" fill="#333">
        <text x="4" y="22">5</text><text x="4" y="50">4</text><text x="4" y="78">3</text><text x="4" y="106">2</text><text x="4" y="134">1</text>
        <text x="20" y="160">Jan</text><text x="38" y="160">Feb</text><text x="56" y="160">Mar</text><text x="74" y="160">Apr</text><text x="92" y="160">May</text><text x="110" y="160">Jun</text><text x="128" y="160">Jul</text><text x="146" y="160">Aug</text><text x="164" y="160">Sep</text><text x="182" y="160">Oct</text><text x="200" y="160">Nov</text><text x="218" y="160">Dec</text>
        <text x="150" y="174">Source: Annual Review 2014</text>
      </g>
      <polyline fill="none" stroke="#25337a" stroke-width="1.5" points="20,140 40,130 60,125 80,118 100,110 120,100 140,92 160,82 180,70 200,55 220,35"/>
      <polyline fill="none" stroke="#3fb6c8" stroke-width="1.5" points="20,138 40,134 60,128 80,126 100,120 120,112 140,108 160,98 180,90 200,80 220,62"/>
      <text x="70" y="62" font-family="Open Sans, sans-serif" font-size="16" font-weight="700" fill="#3fb6c8">2.66</text>
      <text x="62" y="72" font-family="Open Sans, sans-serif" font-size="4.5" fill="#333">Average monthly yield rate</text>
    </svg>
    <p style="position:absolute;left:330px;top:100px;width:210px;font-size:9px;font-weight:700;color:var(--ink);line-height:1.3">This line graph created in Meridian Draw default. You can easily change as appropriate for your data.</p>
    <p class="body-text" style="position:absolute;left:330px;top:148px;width:210px">Yield rose each month as new leases began and vacant units filled. Both lines show the same upward trend, with the second tracking net income after costs. Late year gains came from completed upgrades and stronger rents in core markets.</p>
    <div class="foot-rule"></div>
    <div class="brand"><span class="brand-mark"></span>KEYSTONE HOLDINGS</div>
  </section>

  <section class="slide thanks">
    <div class="thanks-word">THANK YOU</div>
    <div class="thanks-band">
      <div class="social" aria-label="Social links"><span></span><span></span><span></span><span></span><span></span></div>
    </div>
  </section>

</main>
</body>
</html>
```